We need visit card and a letter paper for our website. thx

We have a beauty clinic in Switzerland.
https://wiesentalblick.ch
We need a visit card.

Requirements
Must have
• see colors on website

```html
<!DOCTYPE html>
<html lang="en">
<head>
<meta charset="utf-8">
<title>Wiesentalblick – Stationery</title>
<link rel="stylesheet" href="https://fonts.googleapis.com/css2?family=Open+Sans:wght@400&display=swap">
<style>
  :root {
    --backdrop: #dedede;
    --ink-dark: #29292b;
    --rose: #b95d85;
    --paper: #f9f9f9;
    --body-text: #5a5a5c;
    --header-text: #e6e6e6;
  }
  * { margin: 0; padding: 0; box-sizing: border-box; }
  html, body { width: 1200px; height: 800px; overflow: hidden; }
  body {
    position: relative;
    background: var(--backdrop);
    font-family: "Open Sans", sans-serif;
  }
  .sheet {
    position: absolute;
    width: 407px;
    height: 574px;
    box-shadow: 0 6px 18px rgba(0,0,0,0.18);
  }
  .cover {
    left: 165px; top: 111px;
    background: var(--ink-dark);
    display: flex; align-items: center; justify-content: center;
  }
  .cover-name {
    color: var(--rose);
    font-size: 40px;
    font-weight: 400;
    letter-spacing: 0.5px;
  }
  .letterhead {
    left: 613px; top: 110px;
    background: var(--paper);
  }
  .letter-header {
    height: 72px;
    background: var(--ink-dark);
    position: relative;
  }
  .header-name {
    position: absolute;
    left: 37px; top: 26px;
    color: var(--rose);
    font-size: 14px;
    font-weight: 400;
  }
  .header-address {
    position: absolute;
    left: 172px; top: 25px;
    display: flex; gap: 3px;
    color: var(--header-text);
    font-size: 7.5px;
    line-height: 10px;
  }
  .header-contacts {
    position: absolute;
    left: 268px; top: 20px;
    list-style: none;
    color: var(--header-text);
    font-size: 7.5px;
    line-height: 10.3px;
  }
  .header-contacts li { display: flex; align-items: center; gap: 3px; }
  .icon { width: 7px; height: 7px; flex: none; fill: var(--rose); }
  .icon-pin { width: 6px; height: 8px; margin-top: 1px; }
  .letter-body {
    position: absolute;
    left: 38px; top: 146px;
    width: 334px;
    color: var(--body-text);
    font-size: 7.45px;
    line-height: 11.1px;
  }
  .letter-body p { text-align: justify; margin-bottom: 11px; }
  .letter-body .greeting, .letter-body .closing { text-align: left; }
  .signature {
    width: 48px; height: 44px;
    margin-top: 4px;
    background: linear-gradient(135deg, rgba(41,41,43,0.12), rgba(41,41,43,0.04));
  }
</style>
</head>
<body>
  <section class="sheet cover">
    <span class="cover-name">Wiesentalblick</span>
  </section>

  <section class="sheet letterhead">
    <header class="letter-header">
      <span class="header-name">Wiesentalblick</span>
      <div class="header-address">
        <svg class="icon icon-pin" viewBox="0 0 12 16" aria-hidden="true"><path d="M6 0a6 6 0 0 0-6 6c0 4.5 6 10 6 10s6-5.5 6-10a6 6 0 0 0-6-6zm0 8.5A2.5 2.5 0 1 1 6 3.5a2.5 2.5 0 0 1 0 5z"/></svg>
        <span>Talstrasse 12, 4410<br>Liestal, Switzerland</span>
      </div>
      <ul class="header-contacts">
        <li><svg class="icon" viewBox="0 0 16 16" aria-hidden="true"><path d="M1 6c0-2 3-4 7-4s7 2 7 4v1h-3V5.5H4V7H1zM3 8h10l1 6H2z"/></svg>+41 (0) 800 22 30 40</li>
        <li><svg class="icon" viewBox="0 0 16 16" aria-hidden="true"><path d="M1 4h14v9H1zm1.5 1L8 9l5.5-4z"/></svg>hallo@wiesentalblick.ch</li>
        <li><svg class="icon" viewBox="0 0 16 16" aria-hidden="true"><circle cx="8" cy="8" r="7"/></svg>www.wiesentalblick.ch</li>
      </ul>
    </header>

    <article class="letter-body">
      <p class="greeting">Dear customer,</p>
      <p>Lorem ipsum dolor sit amet, consectetur adipisicing elit, sed do eiusmod tempor incididunt ut labore et dolore magna aliqua. Ut enim ad minim veniam, quis nostrud exercitation ullamco laboris nisi ut aliquip ex ea commodo consequat. Duis aute irure dolor in reprehenderit in voluptate velit esse cillum dolore eu fugiat nulla pariatur. Excepteur sint occaecat cupidatat non proident, sunt in culpa qui officia deserunt mollit anim id est laborum.</p>
      <p>Lorem ipsum dolor sit amet, consectetur adipisicing elit, sed do eiusmod tempor incididunt ut labore et dolore magna aliqua. Ut enim ad minim veniam, quis nostrud exercitation ullamco laboris nisi ut aliquip ex ea commodo consequat. Duis aute irure dolor in reprehenderit in voluptate velit esse cillum dolore eu fugiat nulla pariatur. Excepteur sint occaecat cupidatat non proident, sunt in culpa qui officia deserunt mollit anim id est laborum.</p>
      <p>Lorem ipsum dolor sit amet, consectetur adipisicing elit, sed do eiusmod tempor incididunt ut labore et dolore magna aliqua. Ut enim ad minim veniam, quis nostrud exercitation ullamco laboris nisi ut aliquip ex ea commodo consequat. Duis aute irure dolor in reprehenderit in voluptate velit esse cillum dolore eu fugiat nulla pariatur. Excepteur sint occaecat cupidatat non proident, sunt in culpa qui officia deserunt mollit anim id est laborum.</p>
      <p>Lorem ipsum dolor sit amet, consectetur adipisicing elit, sed do eiusmod tempor incididunt ut labore et dolore magna aliqua. Ut enim ad minim veniam, quis nostrud exercitation ullamco laboris nisi ut aliquip ex ea commodo consequat. Duis aute irure dolor in reprehenderit.</p>
      <p class="closing">Yours Sincerely,</p>
      <div class="signature" role="img" aria-label="Handwritten signature"></div>
    </article>
  </section>
</body>
</html>
```